Plumbing website that stands out

Seo optimized, mobile friendly, easily editable word press Plumbing website with google reviews widget. And widget of revolving photos of completed work. Contact page and services page, about page. Will provide, “About” content. And photos Need all other content written.
Services include:
Water heater replacement
Tankless water heater installation
Kitchen and bath remodel
Drain cleaning and clog removal
Leak repair
Faucet repair and replacement

I will be adding services and photos of recent completed projects as time goes on.

```html
<!DOCTYPE html>
<html lang="en">
<head>
<meta charset="utf-8">
<title>Clearline Plumbing</title>
<link href="https://fonts.googleapis.com/css2?family=Cinzel:wght@500;600&family=Poppins:wght@400;500;600&family=Dancing+Script:wght@600&display=swap" rel="stylesheet">
<style>
:root{
  --blue:#2d62ab;
  --navy:#1f4f8f;
  --deep:#16396b;
  --sky:#4fb1dc;
  --teal:#68c3e3;
  --pale:#eef7fb;
  --ink:#2b2f36;
  --grey:#6a717c;
  --line:#e3e8ee;
  --footer:#23262b;
  --white:#fff;
  --star:#f2b21c;
}
*{box-sizing:border-box;margin:0;padding:0}
html,body{width:1200px;height:5089px;overflow:hidden}
body{font-family:'Poppins',sans-serif;color:var(--ink);background:var(--white);font-size:12px;position:relative}
.serif{font-family:'Cinzel',serif}
.script{font-family:'Dancing Script',cursive;color:var(--sky)}
section,header,footer{position:absolute;left:0;width:1200px}
.abs{position:absolute}
.btn{display:inline-block;background:var(--blue);color:#fff;border-radius:20px;font-size:11px;padding:0 22px;line-height:34px}
/* header */
.site-header{top:0;height:115px;background:#fff}
.brand{left:60px;top:14px;width:180px;text-align:center}
.brand .mark{width:44px;height:44px;margin:0 auto 4px;background:var(--blue);border-radius:4px}
.brand .name{font-family:'Cinzel',serif;font-size:19px;letter-spacing:3px;color:var(--ink);font-weight:600}
.brand .sub{font-size:8px;letter-spacing:6px;color:var(--sky)}
.topbar{top:10px;left:440px;display:flex;gap:24px;font-size:10px;color:var(--grey);align-items:center}
.topbar .stars{color:var(--star);letter-spacing:2px;font-size:12px}
.socials{display:flex;gap:6px}
.socials span{width:24px;height:24px;border-radius:50%;background:var(--sky);display:block}
.socials.light span{background:#fff;border:2px solid var(--blue)}
.nav{top:64px;left:468px;display:flex;gap:36px;font-size:11px;font-weight:500}
.nav .on{color:var(--blue)}
.call{top:56px;left:840px;display:flex;align-items:center;gap:10px}
.call .ic{width:38px;height:38px;border-radius:50%;background:var(--blue);display:flex;align-items:center;justify-content:center}
.call small{display:block;font-size:9px}
.call b{font-size:15px;font-weight:600}
.book{top:56px;left:1024px;width:116px;text-align:center;background:var(--blue);color:#fff;border-radius:20px;line-height:36px;font-size:11px}
/* hero */
.hero{top:115px;height:597px;background:linear-gradient(90deg,#f3f1ee 0%,#ebe8e4 45%,#5e7fa3 70%,#3d5e86 100%)}
.hero .photo{left:0;top:0;width:1200px;height:597px}
.hero .tag{left:60px;top:140px;font-size:22px}
.hero h1{left:62px;top:178px;font-family:'Cinzel',serif;font-weight:500;font-size:50px;line-height:60px;color:var(--ink)}
.hero h1 span{color:var(--blue)}
.hero p{left:62px;top:303px;width:480px;font-size:12px;line-height:20px;color:var(--grey)}
.hero .btn{left:60px;top:378px}
.quick-form{left:60px;top:646px;width:1080px;height:133px;background:var(--sky);border-radius:12px;padding:22px 24px}
.quick-form h2{font-family:'Cinzel',serif;color:#fff;font-weight:500;font-size:26px;margin-bottom:18px}
.quick-form .row{display:flex;gap:12px}
.quick-form .field{background:#fff;height:32px;flex:1;font-size:11px;color:var(--grey);padding:8px 12px}
.quick-form .send{background:var(--blue);color:#fff;width:90px;text-align:center;line-height:32px;font-size:11px;border-radius:3px}
/* about */
.about{top:780px;height:598px}
.about .img1{left:60px;top:63px;width:413px;height:397px;background:linear-gradient(135deg,#cfd3d8,#6d7580)}
.about .img2{left:322px;top:232px;width:300px;height:284px;background:linear-gradient(135deg,#e8f0f6,#6f8ab0);border:8px solid #fff}
.about .txt{left:658px;top:104px;width:482px}
.about .txt .script{font-size:20px}
.about h2{font-family:'Cinzel',serif;font-weight:500;font-size:32px;line-height:46px;margin:6px 0 18px}
.about h2 span{color:var(--blue)}
.about p{font-size:11.5px;line-height:22px;color:var(--grey);margin-bottom:10px}
.about .btn{margin-top:10px}
/* services */
.services{top:1378px;height:500px;background:var(--pale)}
.sec-title{text-align:center;font-family:'Cinzel',serif;font-weight:500;font-size:32px;line-height:46px}
.sec-title span{color:var(--blue)}
.services .sec-title{position:absolute;top:50px;width:100%}
.svc{top:144px;width:252px;height:297px;background:#fff}
.svc .pic{height:206px;background:linear-gradient(135deg,#c9d1da,#4f5d6e)}
.svc .badge{position:absolute;left:104px;top:182px;width:46px;height:46px;border-radius:50%;background:var(--teal);border:3px solid #fff}
.svc h3{font-family:'Cinzel',serif;font-weight:500;text-align:center;font-size:15px;line-height:22px;margin-top:34px}
.svc.active{background:var(--blue);color:#fff;text-align:center;padding:40px 26px 0}
.svc.active .badge{top:-24px}
.svc.active h3{margin:0 0 8px}
.svc.active p{font-size:11px;line-height:22px}
.svc.active a{color:var(--teal);font-size:11px;text-decoration:underline}
.arrow{width:30px;height:30px;border-radius:50%;background:var(--blue);display:flex;align-items:center;justify-content:center}
.services .arrow{background:var(--navy)}
/* why */
.why{top:1878px;height:530px;background:var(--blue)}
.why .photo{left:600px;top:0;width:600px;height:530px;background:linear-gradient(90deg,rgba(45,98,171,0),#8ea4be 40%,#e6e9ee 100%)}
.why h2{left:62px;top:58px;font-family:'Cinzel',serif;color:#fff;font-weight:500;font-size:32px;line-height:46px}
.why .item{display:flex;align-items:center;gap:24px;color:#fff;font-family:'Cinzel',serif;font-size:14px;line-height:22px;width:300px}
.why .circ{width:74px;height:74px;border-radius:50%;background:var(--sky);border:4px solid rgba(255,255,255,.35);display:flex;align-items:center;justify-content:center;flex:none}
/* testimonials */
.reviews{top:2408px;height:587px;overflow:hidden}
.reviews .sec-title{position:absolute;top:70px;width:100%}
.card{top:202px;width:328px;height:302px;background:#fff;box-shadow:0 0 14px rgba(0,0,0,.1);text-align:center;padding:40px 30px}
.card .avatar{width:52px;height:52px;border-radius:50%;background:#d9c9bd;margin:0 auto 10px}
.card h4{color:var(--blue);font-weight:500;font-size:14px}
.card .stars{color:var(--star);font-size:13px;letter-spacing:3px;margin:4px 0 18px}
.card p{font-size:11px;line-height:21px;color:var(--grey)}
/* projects */
.projects{top:2995px;height:781px;border-top:1px solid var(--line);border-bottom:1px solid var(--line)}
.projects .sec-title{position:absolute;top:68px;width:100%}
.tile{width:252px;height:224px}
.tile.hover{background:var(--blue);display:flex;align-items:center;justify-content:center}
.projects .btn{left:554px;top:688px}
/* areas */
.areas{top:3776px;height:696px}
.areas h2{left:84px;top:215px;font-family:'Cinzel',serif;font-weight:500;font-size:32px;color:var(--blue)}
.areas ul{list-style:none;top:282px;font-size:11px;color:var(--grey)}
.areas li{display:flex;align-items:center;gap:12px;height:33px}
.map{left:510px;top:100px;width:630px;height:506px;background:linear-gradient(135deg,#eef1f3,#e2e7ea);border:1px solid var(--line)}
/* appointment */
.appt{top:4472px;height:303px;background:var(--blue);color:#fff;text-align:center}
.appt h2{position:absolute;top:58px;width:100%;font-family:'Cinzel',serif;font-weight:500;font-size:32px;line-height:42px}
.appt p{position:absolute;top:148px;width:100%;font-size:14px}
.appt .acts{position:absolute;top:202px;left:383px;display:flex;align-items:center;gap:32px}
.appt .cta{background:var(--teal);border-radius:20px;line-height:36px;padding:0 26px;font-size:12px}
.appt .or{font-family:'Dancing Script',cursive;font-size:28px}
.appt .help{display:flex;align-items:center;gap:14px;text-align:left}
.appt .help .ic{width:44px;height:44px;border-radius:50%;background:var(--teal);border:3px solid rgba(255,255,255,.5);display:flex;align-items:center;justify-content:center}
.appt .help small{display:block;font-size:11px}
.appt .help b{font-size:18px;font-weight:600}
/* footer */
.site-footer{top:4775px;height:286px;background:var(--footer);color:#fff}
.site-footer .brand{left:60px;top:44px;width:200px}
.site-footer .brand .name{color:#fff;font-size:24px}
.site-footer .brand .mark{width:70px;height:70px;background:#fff}
.site-footer .socials{justify-content:center;margin-top:16px}
.fcol{top:50px}
.fcol h5{font-family:'Cinzel',serif;font-weight:500;color:var(--teal);font-size:12px;margin-bottom:16px}
.fcol li{list-style:none;font-size:11px;line-height:28px}
.fcol .ci{display:flex;gap:12px;align-items:flex-start;margin-bottom:14px;font-size:11px;line-height:18px;width:230px}
.fcol .ci span{width:28px;height:28px;border-radius:50%;background:var(--teal);flex:none;display:flex;align-items:center;justify-content:center}
.copy{top:5061px;height:28px;background:var(--blue);color:#fff;text-align:center;font-size:10px;line-height:28px}
</style>
</head>
<body>

<header class="site-header">
  <div class="brand abs"><div class="mark"></div><div class="name">CLEARLINE</div><div class="sub">PLUMBING</div></div>
  <div class="topbar abs"><span><span class="stars">★★★★★</span>&nbsp; 5 Star Reviews For Our Services.</span><span>◷ &nbsp;Opening Hours <span style="color:var(--sky)">Mon To Sun 24/7</span></span><div class="socials"><span></span><span></span><span></span><span></span></div></div>
  <nav class="nav abs"><span class="on">HOME</span><span>ABOUT</span><span>SERVICES</span><span>CONTACT US</span></nav>
  <div class="call abs"><div class="ic"><svg width="18" height="18" viewBox="0 0 24 24" fill="#fff"><path d="M6.6 10.8a15 15 0 0 0 6.6 6.6l2.2-2.2c.3-.3.7-.4 1-.2 1.1.4 2.3.6 3.6.6.6 0 1 .4 1 1V20c0 .6-.4 1-1 1A17 17 0 0 1 3 4c0-.6.4-1 1-1h3.5c.6 0 1 .4 1 1 0 1.3.2 2.5.6 3.6.1.3 0 .7-.2 1z"/></svg></div><div><small>Call Us Now</small><b>123 456 7890</b></div></div>
  <div class="book abs">Book Now</div>
</header>

<section class="hero">
  <div class="photo abs" role="img" aria-label="Plumber fixing a kitchen sink tap with a tool belt"></div>
  <div class="tag abs script">Clearline Plumbing Sydney</div>
  <h1 class="abs">BEST AND FAST<br><span>PLUMBING SERVICES</span></h1>
  <p class="abs">Lorem Ipsum is simply dummy text of the printing and typesetting industry. Lorem Ipsum has been the industry's.</p>
  <span class="btn abs">Request Services</span>
</section>

<form class="quick-form abs">
  <h2>CONTACT CLEARLINE PLUMBING SERVICES</h2>
  <div class="row"><div class="field">Name*</div><div class="field">E-mail*</div><div class="field">Phone No.*</div><div class="field" style="flex:1.05">Massage*</div><div class="send">Send</div></div>
</form>

<section class="about">
  <div class="img1 abs" role="img" aria-label="Plumber kneeling to inspect pipes under a sink"></div>
  <div class="img2 abs" role="img" aria-label="Two plumbers standing with arms crossed beside a van"></div>
  <div class="txt abs">
    <div class="script">Who We Are</div>
    <h2>WELCOME TO <span>CLEARLINE<br>PLUMBING</span></h2>
    <p>Lorem Ipsum is simply dummy text of the printing and typesetting industry. Lorem Ipsum has been the industry's standard dummy text ever since the 1500s, when an unknown printer took a galley of type and scrambled it to make a type specimen book. It has survived not only five centuries, but also the leap into electronic typesetting, remaining essentially unchanged.</p>
    <p>Lorem Ipsum is simply dummy text of the printing and typesetting industry. Lorem Ipsum has been the industry's standard dummy text.</p>
    <span class="btn">Learn More</span>
  </div>
</section>

<section class="services">
  <h2 class="sec-title">OUR <span>SERVICES</span></h2>
  <div class="arrow abs" style="left:16px;top:252px"><svg width="12" height="12" viewBox="0 0 12 12"><path d="M8 2 4 6l4 4" stroke="#fff" stroke-width="2" fill="none"/></svg></div>
  <div class="arrow abs" style="left:1152px;top:252px"><svg width="12" height="12" viewBox="0 0 12 12"><path d="M4 2l4 4-4 4" stroke="#fff" stroke-width="2" fill="none"/></svg></div>
  <div class="svc abs" style="left:60px"><div class="pic" role="img" aria-label="Technician servicing a water heater"></div><div class="badge"></div><h3>WATER HEATER<br>REPLACEMENT</h3></div>
  <div class="svc abs active" style="left:336px"><div class="badge"></div><h3>TANKLESS WATER HEATER<br>INSTALLATION</h3><p>Lorem Ipsum is simply dummy text of the printing and typesetting industry. Lorem Ipsum has been the industry's standard dummy text.</p><a>Learn More</a></div>
  <div class="svc abs" style="left:612px"><div class="pic" role="img" aria-label="Modern white bathroom basin with tap" style="background:linear-gradient(135deg,#f4f5f6,#9aa3ad)"></div><div class="badge"></div><h3>KITCHEN AND<br>BATH REMODEL</h3></div>
  <div class="svc abs" style="left:888px"><div class="pic" role="img" aria-label="Plumber clearing a kitchen sink drain"></div><div class="badge"></div><h3>DRAIN CLEANING<br>AND CLOG REMOVAL</h3></div>
</section>

<section class="why">
  <div class="photo abs" role="img" aria-label="Smiling plumber in overalls standing in front of a company van"></div>
  <h2 class="abs">WHY CHOOSE<br>CLEARLINE PLUMBING</h2>
  <div class="item abs" style="left:60px;top:192px"><div class="circ"><svg width="34" height="34" viewBox="0 0 24 24" fill="none" stroke="#fff" stroke-width="1.6"><circle cx="12" cy="12" r="9"/><path d="M12 7v5l3 2"/></svg></div>ON TIME EVERY<br>TIME</div>
  <div class="item abs" style="left:355px;top:192px"><div class="circ"><svg width="34" height="34" viewBox="0 0 24 24" fill="none" stroke="#fff" stroke-width="1.6"><circle cx="12" cy="8" r="4"/><path d="M4 21c1-5 15-5 16 0"/></svg></div>HIGHLY TRAINED<br>PLUMBERS</div>
  <div class="item abs" style="left:60px;top:294px"><div class="circ"><svg width="34" height="34" viewBox="0 0 24 24" fill="none" stroke="#fff" stroke-width="1.6"><path d="M4 12h16M12 4v16"/><circle cx="12" cy="12" r="9"/></svg></div>FIXED PRICE<br>REPAIRS</div>
  <div class="item abs" style="left:355px;top:294px"><div class="circ"><svg width="34" height="34" viewBox="0 0 24 24" fill="none" stroke="#fff" stroke-width="1.6"><circle cx="12" cy="12" r="9"/><circle cx="12" cy="12" r="5"/></svg></div>TOTAL WORK<br>GAURANTEE</div>
  <div class="item abs" style="left:60px;top:388px"><div class="circ"><svg width="34" height="34" viewBox="0 0 24 24" fill="none" stroke="#fff" stroke-width="1.8"><circle cx="12" cy="12" r="9"/><path d="m8 12 3 3 5-6"/></svg></div>RESPECT FOR<br>YOUR HOME</div>
</section>

<section class="reviews">
  <h2 class="sec-title">WHAT OUR<br><span>CUSTOMER ARE SAYS...</span></h2>
  <div class="card abs" style="left:-272px"><div class="avatar"></div><h4>Client Name</h4><div class="stars">★★★★★</div><p>Lorem Ipsum is simply dummy text of the printing and typesetting industry. Lorem Ipsum has been the industry's standard dummy text ever since the 1500s.</p></div>
  <div class="card abs" style="left:79px"><div class="avatar"></div><h4>Client Name</h4><div class="stars">★★★★★</div><p>Lorem Ipsum is simply dummy text of the printing and typesetting industry. Lorem Ipsum has been the industry's standard dummy text ever since the 1500s, when an unknown printer took a galley of type...</p></div>
  <div class="card abs" style="left:431px"><div class="avatar"></div><h4>Client Name</h4><div class="stars">★★★★★</div><p>Lorem Ipsum is simply dummy text of the printing and typesetting industry. Lorem Ipsum has been the industry's standard dummy text ever since the 1500s, when an unknown printer took a galley of type...</p></div>
  <div class="card abs" style="left:785px"><div class="avatar"></div><h4>Client Name</h4><div class="stars">★★★★★</div><p>Lorem Ipsum is simply dummy text of the printing and typesetting industry. Lorem Ipsum has been the industry's standard dummy text ever since the 1500s, when an unknown printer took a galley of type...</p></div>
  <div class="card abs" style="left:1138px"><div class="avatar"></div><h4>Client Name</h4></div>
  <div class="arrow abs" style="left:52px;top:346px"><svg width="14" height="12" viewBox="0 0 14 12"><path d="M13 6H2M6 1 1 6l5 5" stroke="#fff" stroke-width="1.8" fill="none"/></svg></div>
  <div class="arrow abs" style="left:1110px;top:346px"><svg width="14" height="12" viewBox="0 0 14 12"><path d="M1 6h11M8 1l5 5-5 5" stroke="#fff" stroke-width="1.8" fill="none"/></svg></div>
</section>

<section class="projects">
  <h2 class="sec-title">RECENT COMPLETED<br><span>PROJECTS</span></h2>
  <div class="tile abs" style="left:60px;top:176px;background:linear-gradient(135deg,#f7f7f7,#bfc3c7)" role="img" aria-label="White panel radiator"></div>
  <div class="tile abs hover" style="left:336px;top:176px"><svg width="32" height="32" viewBox="0 0 32 32" fill="none" stroke="#fff" stroke-width="1.5"><circle cx="16" cy="16" r="14"/><path d="M16 10v12M10 16h12"/></svg></div>
  <div class="tile abs" style="left:612px;top:176px;background:linear-gradient(135deg,#3d3d3f,#c7c9cc)" role="img" aria-label="Kitchen sink with tall chrome tap"></div>
  <div class="tile abs" style="left:888px;top:176px;background:radial-gradient(circle,#7b8087,#e9eaec 60%)" role="img" aria-label="Close-up of a steel sink drain"></div>
  <div class="tile abs" style="left:60px;top:421px;background:linear-gradient(135deg,#4e77b3,#b8c6d6)" role="img" aria-label="Hand tightening a pipe with a wrench"></div>
  <div class="tile abs" style="left:336px;top:421px;background:linear-gradient(135deg,#2f5f3a,#202224)" role="img" aria-label="Black kitchen tap over a sink"></div>
  <div class="tile abs" style="left:612px;top:421px;background:linear-gradient(135deg,#b4775a,#e8e3df)" role="img" aria-label="Electric shower unit on a tiled wall"></div>
  <div class="tile abs" style="left:888px;top:421px;background:linear-gradient(135deg,#2d4d77,#d2cfca)" role="img" aria-label="Freestanding bathtub in a blue bathroom"></div>
  <span class="btn abs">View All</span>
</section>

<section class="areas">
  <h2 class="abs">SERVICES AREAS</h2>
  <ul class="abs" style="left:84px">
    <li><svg width="16" height="18" viewBox="0 0 16 18" fill="none" stroke="#555" stroke-width="1.4"><path d="M8 16s-5-5-5-9a5 5 0 0 1 10 0c0 4-5 9-5 9z"/><circle cx="8" cy="7" r="2"/></svg>Lorem Ipsum is simply</li>
    <li><svg width="16" height="18" viewBox="0 0 16 18" fill="none" stroke="#555" stroke-width="1.4"><path d="M8 16s-5-5-5-9a5 5 0 0 1 10 0c0 4-5 9-5 9z"/><circle cx="8" cy="7" r="2"/></svg>Lorem Ipsum is simply</li>
    <li><svg width="16" height="18" viewBox="0 0 16 18" fill="none" stroke="#555" stroke-width="1.4"><path d="M8 16s-5-5-5-9a5 5 0 0 1 10 0c0 4-5 9-5 9z"/><circle cx="8" cy="7" r="2"/></svg>Lorem Ipsum is simply</li>
    <li><svg width="16" height="18" viewBox="0 0 16 18" fill="none" stroke="#555" stroke-width="1.4"><path d="M8 16s-5-5-5-9a5 5 0 0 1 10 0c0 4-5 9-5 9z"/><circle cx="8" cy="7" r="2"/></svg>Lorem Ipsum is simply</li>
    <li><svg width="16" height="18" viewBox="0 0 16 18" fill="none" stroke="#555" stroke-width="1.4"><path d="M8 16s-5-5-5-9a5 5 0 0 1 10 0c0 4-5 9-5 9z"/><circle cx="8" cy="7" r="2"/></svg>Lorem Ipsum is simply</li>
    <li><svg width="16" height="18" viewBox="0 0 16 18" fill="none" stroke="#555" stroke-width="1.4"><path d="M8 16s-5-5-5-9a5 5 0 0 1 10 0c0 4-5 9-5 9z"/><circle cx="8" cy="7" r="2"/></svg>Lorem Ipsum is simply</li>
    <li><svg width="16" height="18" viewBox="0 0 16 18" fill="none" stroke="#555" stroke-width="1.4"><path d="M8 16s-5-5-5-9a5 5 0 0 1 10 0c0 4-5 9-5 9z"/><circle cx="8" cy="7" r="2"/></svg>Lorem Ipsum is simply</li>
  </ul>
  <ul class="abs" style="left:300px">
    <li><svg width="16" height="18" viewBox="0 0 16 18" fill="none" stroke="#555" stroke-width="1.4"><path d="M8 16s-5-5-5-9a5 5 0 0 1 10 0c0 4-5 9-5 9z"/><circle cx="8" cy="7" r="2"/></svg>Lorem Ipsum is simply</li>
    <li><svg width="16" height="18" viewBox="0 0 16 18" fill="none" stroke="#555" stroke-width="1.4"><path d="M8 16s-5-5-5-9a5 5 0 0 1 10 0c0 4-5 9-5 9z"/><circle cx="8" cy="7" r="2"/></svg>Lorem Ipsum is simply</li>
    <li><svg width="16" height="18" viewBox="0 0 16 18" fill="none" stroke="#555" stroke-width="1.4"><path d="M8 16s-5-5-5-9a5 5 0 0 1 10 0c0 4-5 9-5 9z"/><circle cx="8" cy="7" r="2"/></svg>Lorem Ipsum is simply</li>
    <li><svg width="16" height="18" viewBox="0 0 16 18" fill="none" stroke="#555" stroke-width="1.4"><path d="M8 16s-5-5-5-9a5 5 0 0 1 10 0c0 4-5 9-5 9z"/><circle cx="8" cy="7" r="2"/></svg>Lorem Ipsum is simply</li>
    <li><svg width="16" height="18" viewBox="0 0 16 18" fill="none" stroke="#555" stroke-width="1.4"><path d="M8 16s-5-5-5-9a5 5 0 0 1 10 0c0 4-5 9-5 9z"/><circle cx="8" cy="7" r="2"/></svg>Lorem Ipsum is simply</li>
    <li><svg width="16" height="18" viewBox="0 0 16 18" fill="none" stroke="#555" stroke-width="1.4"><path d="M8 16s-5-5-5-9a5 5 0 0 1 10 0c0 4-5 9-5 9z"/><circle cx="8" cy="7" r="2"/></svg>Lorem Ipsum is simply</li>
    <li><svg width="16" height="18" viewBox="0 0 16 18" fill="none" stroke="#555" stroke-width="1.4"><path d="M8 16s-5-5-5-9a5 5 0 0 1 10 0c0 4-5 9-5 9z"/><circle cx="8" cy="7" r="2"/></svg>Lorem Ipsum is simply</li>
  </ul>
  <div class="map abs" role="img" aria-label="Street map of the service area"></div>
</section>

<section class="appt">
  <h2>WOULD YOU LIKE TO SET UP AN<br>APPOINTMENT WITH CLEARLINE PLUMBING</h2>
  <p>We Will be in Touuch with you to verify your appointment.</p>
  <div class="acts">
    <span class="cta">Contact Us Today</span>
    <span class="or">Or</span>
    <div class="help"><div class="ic"><svg width="20" height="20" viewBox="0 0 24 24" fill="#fff"><path d="M6.6 10.8a15 15 0 0 0 6.6 6.6l2.2-2.2c.3-.3.7-.4 1-.2 1.1.4 2.3.6 3.6.6.6 0 1 .4 1 1V20c0 .6-.4 1-1 1A17 17 0 0 1 3 4c0-.6.4-1 1-1h3.5c.6 0 1 .4 1 1 0 1.3.2 2.5.6 3.6.1.3 0 .7-.2 1z"/></svg></div><div><small>Need Help You</small><b>123 456 7890</b></div></div>
  </div>
</section>

<footer class="site-footer">
  <div class="brand abs"><div class="mark"></div><div class="name">CLEARLINE</div><div class="sub">PLUMBING</div><div class="socials"><span></span><span></span><span></span><span></span></div></div>
  <div class="fcol abs" style="left:336px"><h5>SITE MAP</h5><ul><li>HOME</li><li>ABOUT</li><li>SERVICES</li><li>CONTACT US</li></ul></div>
  <div class="fcol abs" style="left:612px"><h5>SERVICES</h5><ul><li>Water heater replacement</li><li>Tankless water heater installation</li><li>Kitchen and bath remodel</li><li>Drain cleaning and clog removal</li><li>Leak repair</li></ul></div>
  <div class="fcol abs" style="left:888px"><h5>CONTACT US</h5>
    <div class="ci"><span><svg width="12" height="14" viewBox="0 0 16 18" fill="none" stroke="#fff" stroke-width="1.8"><path d="M8 16s-5-5-5-9a5 5 0 0 1 10 0c0 4-5 9-5 9z"/></svg></span>123, Lorem Ipsum is a dummy text.</div>
    <div class="ci"><span><svg width="12" height="12" viewBox="0 0 24 24" fill="#fff"><path d="M6.6 10.8a15 15 0 0 0 6.6 6.6l2.2-2.2c.3-.3.7-.4 1-.2 1.1.4 2.3.6 3.6.6.6 0 1 .4 1 1V20c0 .6-.4 1-1 1A17 17 0 0 1 3 4c0-.6.4-1 1-1h3.5c.6 0 1 .4 1 1 0 1.3.2 2.5.6 3.6.1.3 0 .7-.2 1z"/></svg></span>123 456 7890</div>
    <div class="ci"><span><svg width="13" height="10" viewBox="0 0 16 12" fill="none" stroke="#fff" stroke-width="1.6"><rect x="1" y="1" width="14" height="10"/><path d="m1 1 7 6 7-6"/></svg></span>info@clearlineplumbing.com</div>
  </div>
</footer>
<div class="copy abs" style="left:0;width:1200px">©2023 CLEARLINE PLUMBING. All rights reserved. | Privacy Policy | Terms and Conditions</div>

</body>
</html>
```